Pellmore Dental Children's postcard before camp starts

Families are starting to prep their children to go to camp. Sometimes parents forget to have a dental check up during the year and we always have emergencies coming into the office during the summer time.

Pellmore Dental is looking to create a Mailing Postcard to send our community targeting Parents (specifically mothers) to remind them that having a dental check up for their children before camp starts is very important.

We would like to send out the cards to our entire community (over 2000 homes) and so we are looking for a creative design that will have the parents calling us to schedule an appointment for their children before the camp season starts.

We have included a few post cards that we found online that resemble what we are looking for

Its the end of the school year and the start of the summer season so we are looking for a nice summer look and feel.

Younger children need check up and cleanings, teens who play sports should wear sports guards etc.

Target Market(s)

We are targeting mothers/parents with children ages 2-13 in our community

Industry/Entity Type

Dental

Font styles to use
Other font styles liked:
• I do not have a fond in mind but something for children.

Requirements
Must have
• We must have our office information (ie: Logo, telephone number, address). we would love to have children smiling on the cards. We would love to have something look like the "Sprig" pediatric dental.
Nice to have
• front and back side with nice art work,
Should not have
• this is a target for children. Please keep it friendly and fresh looking.

```html
<!DOCTYPE html>
<html lang="en">
<head>
<meta charset="UTF-8">
<title>Pellmore Dental – Summer Camp Check-up Postcard</title>
<link rel="stylesheet" href="https://fonts.googleapis.com/css2?family=Libre+Baskerville&family=Open+Sans:wght@600&display=swap">
<style>
  :root {
    --page-bg: #f4f4f4;
    --card-grey: #e6e6e6;
    --card-grey-dark: #d6d6d6;
    --panel-white: #ffffff;
    --ribbon-yellow: #f5c31e;
    --ribbon-yellow-dark: #e8aa08;
    --ribbon-pink: #d8336a;
    --ribbon-pink-dark: #b41f55;
    --ribbon-blue: #1e88e0;
    --ribbon-blue-dark: #0f63b0;
    --brand-blue: #1f7fc2;
    --label-black: #050505;
    --silver-light: #f2f2f2;
    --silver-dark: #b9b9b9;
  }
  * { box-sizing: border-box; margin: 0; padding: 0; }
  html, body { width: 1200px; height: 1000px; overflow: hidden; }
  body { background: var(--page-bg); position: relative; font-family: "Libre Baskerville", Georgia, serif; }

  .postcard {
    position: absolute; left: 60px; top: 130px; width: 1080px; height: 720px;
    background: linear-gradient(135deg, var(--card-grey) 0%, var(--card-grey-dark) 100%);
    box-shadow: 0 6px 18px rgba(0,0,0,.18);
  }

  .info-panel {
    position: absolute; left: 90px; top: 0; width: 360px; height: 660px;
    background: var(--panel-white);
    box-shadow: 4px 6px 14px rgba(0,0,0,.22);
  }
  .ribbons { position: absolute; left: -40px; top: 20px; width: 460px; height: 330px; overflow: visible; }

  .contact-phone {
    position: absolute; left: 30px; top: 172px;
    color: #fff; font-size: 27px; transform: rotate(4deg); transform-origin: left;
  }
  .contact-web {
    position: absolute; left: 20px; top: 266px;
    color: #fff; font-size: 15px; letter-spacing: 1px; transform: rotate(4deg); transform-origin: left;
  }
  .tag {
    position: absolute; background: var(--label-black); color: #fff;
    font-family: "Open Sans", Arial, sans-serif; font-weight: 600; font-size: 15px;
    padding: 6px 20px 6px 12px;
  }
  .tag-phone { left: 30px; top: 130px; width: 96px; transform: rotate(4deg); }
  .tag-web { left: 290px; top: 290px; width: 96px; transform: rotate(4deg); }

  .brand-lockup {
    position: absolute; left: 60px; top: 455px;
    display: flex; align-items: center; gap: 14px;
    color: var(--brand-blue); font-size: 30px; line-height: 1.05;
  }
  .brand-dot { width: 44px; height: 44px; border-radius: 50%; background: var(--brand-blue); flex: none; }

  .headline {
    position: absolute; left: 600px; top: 130px; width: 460px;
    color: var(--brand-blue); font-size: 60px; line-height: 1.1; text-align: center;
    letter-spacing: 2px; text-transform: uppercase;
  }

  .photo-band {
    position: absolute; left: 540px; top: 320px; width: 520px; height: 220px;
    background: linear-gradient(180deg, var(--silver-light), var(--silver-dark));
    box-shadow: 0 4px 10px rgba(0,0,0,.2);
    display: flex; gap: 24px; align-items: center; justify-content: center;
  }
  .photo {
    width: 205px; height: 160px; border: 5px solid #fff;
    box-shadow: 0 3px 8px rgba(0,0,0,.25);
  }
  .photo-toddler { background: linear-gradient(160deg, #6f7f4a, #3d4a63); }
  .photo-boy { background: linear-gradient(160deg, #d9a861, #4a54a8); }
</style>
</head>
<body>
  <section class="postcard">
    <div class="info-panel">
      <svg class="ribbons" viewBox="0 0 460 330" aria-hidden="true">
        <polygon points="30,30 440,60 440,150 30,95" fill="var(--ribbon-yellow)"/>
        <polygon points="440,60 440,150 455,150 455,65" fill="var(--ribbon-yellow-dark)"/>
        <polygon points="20,110 420,170 420,260 20,190" fill="var(--ribbon-pink)"/>
        <polygon points="20,190 20,205 40,193" fill="var(--ribbon-pink-dark)"/>
        <polygon points="10,235 410,275 410,325 10,280" fill="var(--ribbon-blue)"/>
        <polygon points="10,280 10,300 35,283" fill="var(--ribbon-blue-dark)"/>
      </svg>
      <span class="tag tag-phone">PH:</span>
      <p class="contact-phone">(555) 014-2290</p>
      <p class="contact-web">PELLMOREDENTAL.COM</p>
      <span class="tag tag-web">WEB:</span>

      <div class="brand-lockup">
        <span class="brand-dot"></span>
        <span class="brand-name">Pellmore<br>Dental</span>
      </div>
    </div>

    <h1 class="headline">Pellmore Dental</h1>

    <div class="photo-band">
      <div class="photo photo-toddler" role="img" aria-label="Photo of a laughing toddler lying on the grass"></div>
      <div class="photo photo-boy" role="img" aria-label="Photo of a smiling young boy"></div>
    </div>
  </section>
</body>
</html>
```